Brook & Thistle Labels*

Hello :) I am needing labels for my herbal tea/petal product. I am a small producer for the local restaurants (edible flowers/micro herbs & dried product). I am hoping to sell the dried product online. It will be sold in batches as it is ready so quite small/boutique and the label needs to be somewhat generic for the range of produce I make.
Feels: no/minimal plastic, product is in a reusable mason jar, we use organic/regenerative principles from soil health to end product. Treading gently on the land. High quality i.e only fresh hand picked leaf tips for the tea.

```html
<!DOCTYPE html>
<html lang="en">
<head>
<meta charset="utf-8">
<title>Brook &amp; Thistle – Tea Box Label</title>
<link rel="stylesheet" href="https://fonts.googleapis.com/css2?family=Archivo:wdth,wght@100..125,700..900&family=Jost:wght@400&family=Carlito&display=swap">
<style>
  :root {
    --bg: #ece7df;
    --box: #232323;
    --rust: #b5582a;
    --rust-headline: #a85a34;
    --leaf-green: #64a035;
    --band-text: #ececec;
    --rule: #f2f2f2;
  }
  * { margin: 0; padding: 0; box-sizing: border-box; }
  html, body { width: 1200px; height: 1000px; overflow: hidden; }
  body { background: var(--bg); position: relative; }

  .panel {
    position: absolute;
    top: 232px;
    width: 340px;
    height: 474px;
    background: var(--box);
    color: var(--rule);
  }
  .panel--front { left: 292px; }
  .panel--back { left: 718px; }

  .brand-top {
    position: absolute;
    top: 6px; left: 0; right: 0;
    text-align: center;
    font-family: "Archivo", sans-serif;
    font-weight: 900;
    font-stretch: 125%;
    font-size: 17px;
    letter-spacing: 1px;
    color: var(--rust);
  }

  .brand-mark {
    position: absolute;
    left: 0; right: 0;
    display: flex;
    flex-direction: column;
    align-items: center;
    gap: 10px;
  }
  .panel--front .brand-mark { top: 78px; }
  .panel--back .brand-mark { top: 62px; }
  .brand-mark__dot {
    width: 34px; height: 34px;
    border-radius: 50%;
    background: var(--leaf-green);
  }
  .brand-mark__name {
    font-family: "Jost", sans-serif;
    font-weight: 400;
    font-size: 15px;
    color: var(--rust);
  }

  .headline {
    position: absolute;
    left: 25px; top: 222px;
    font-family: "Archivo", sans-serif;
    font-weight: 800;
    font-size: 43px;
    line-height: 1.08;
    color: var(--rust-headline);
  }

  .origin-band {
    position: absolute;
    left: 0; right: 0; top: 351px;
    height: 74px;
    background: var(--leaf-green);
    padding: 6px 26px;
    font-family: "Archivo", sans-serif;
    font-weight: 700;
    font-size: 15.5px;
    line-height: 21px;
    color: var(--band-text);
  }

  .product-table {
    position: absolute;
    left: 75px; top: 171px;
    width: 190px;
    border-collapse: collapse;
    font-family: "Carlito", sans-serif;
    font-size: 10px;
    line-height: 15px;
    color: var(--rule);
  }
  .product-table td {
    border: 1px solid var(--rule);
    padding: 1px 4px;
    vertical-align: middle;
  }
  .product-table .cell-title { text-align: center; height: 31px; }
  .product-table .cell-label { width: 67px; }
  .product-table .row-base td { height: 49px; }
  .product-table .row-short td { height: 30px; }

  .address-note {
    position: absolute;
    left: 40px; right: 40px; top: 424px;
    text-align: center;
    font-family: "Archivo", sans-serif;
    font-weight: 700;
    font-size: 5px;
    line-height: 6px;
    text-transform: uppercase;
    color: var(--rule);
  }
</style>
</head>
<body>

  <section class="panel panel--front">
    <div class="brand-top">FERNHOLLOW</div>
    <div class="brand-mark">
      <span class="brand-mark__dot"></span>
      <span class="brand-mark__name">fernhollow</span>
    </div>
    <h1 class="headline">BROOK<br>&amp; THISTLE</h1>
    <p class="origin-band">GROWN, HARVESTED &amp; DRIED<br>CHEMICAL FREE ON OUR FARM<br>IN EAST GIPPSLAND</p>
  </section>

  <section class="panel panel--back">
    <div class="brand-top">FERNHOLLOW</div>
    <div class="brand-mark">
      <span class="brand-mark__dot"></span>
      <span class="brand-mark__name">fernhollow</span>
    </div>
    <table class="product-table">
      <tr><td class="cell-title" colspan="2">Single Origin<br>Herbal Tea etc.</td></tr>
      <tr class="row-base"><td class="cell-label">Leaf<br>Base:</td><td>Lemon Verbena<br>Mint<br>Agastache</td></tr>
      <tr class="row-short"><td class="cell-label">Petals:</td><td></td></tr>
      <tr class="row-short"><td class="cell-label">Batch:</td><td></td></tr>
      <tr class="row-short"><td colspan="2">Tallow Creek<br>Victoria Australia</td></tr>
    </table>
    <p class="address-note">Full address<br>Packed by hand in small seasonal batches on our farm, Tallow Creek Road,<br>East Gippsland, Victoria Australia. Reuse your jar.</p>
  </section>

</body>
</html>
```